"loop-CAST." SoCal's Fishing Industry's single stop for the latest products, content, and services

Hi, looking for a website design for new LA based company called "loop-CAST." Where we showcase all the latest and greatest products, services, and content in a highly visually appealing platform for all fishing manufacturers and service providers as they relate to the fishing community (manufactures and service providers pay for cost-tiered content exposure and marketing, free exposure for manufacturers and service providers will have affiliate marketing link at minimal content exposure). As well, looking to include an in-site blog, store-products, and media content such as articles, video edits, and fishing condition picture galleries. Visually, looking for a minimalist/clean/blocked/ filterable and visually captivating gallery. Looking for a color pallet with white-background, deep blue- primary, light gray- secondary, light sky blue- third. Style- cleanliness and structure of widgetrove.example meets content like kpwildwater.example.

Target Market(s)

Primary- Southern California/Southwest Fishing Community, Secondary- All other US Fishing Communities

Coding

Coded - Design and coding required

Number of Pages Required

5+ page

Font styles to use
Sans Serif

Colors
959595
86cfc6
cadf82
333333
0555a3

Requirements
Must have
• Fast loading, mobile friendly, Analytics page, email sign up link for emailed newsletter (that is not a full page pop-up but integrated into browse bar), integrated social media links, search bar, filter link, home page return link, minimalist and clean design. Formatted to product showcase website style- please see attached files for ideas for design format and word-logo.
Should not have
• No Clutter, No background advertisements, No long text scripts outside of products main page,

```html
<!DOCTYPE html>
<html lang="en">
<head>
<meta charset="utf-8">
<title>loop-CAST. — Fishing products, content and services</title>
<link href="https://fonts.googleapis.com/css2?family=Montserrat:wght@400;500;600;700;800&family=Open+Sans:wght@400;600;700&display=swap" rel="stylesheet">
<style>
:root{
  --deep-blue:#0555a3;
  --navy:#0b3f86;
  --sky:#86cfc6;
  --lime:#cadf82;
  --ink:#333333;
  --muted:#959595;
  --light-gray:#ececec;
  --panel:#f4f4f4;
  --white:#ffffff;
  --dark:#151515;
  --orange:#f2a23a;
  --green:#3cb878;
  --red:#e0334c;
  --star:#f5b400;
}
*{box-sizing:border-box;margin:0;padding:0}
html,body{width:1200px;height:4700px;overflow:hidden}
body{position:relative;background:var(--white);font-family:"Open Sans",Arial,sans-serif;color:var(--ink)}
.abs{position:absolute}
.heading{font-family:"Montserrat",Arial,sans-serif;font-weight:600;letter-spacing:1px;color:var(--ink)}
.heading b{color:var(--deep-blue);font-weight:600}
.btn{position:absolute;display:flex;align-items:center;justify-content:center;font-family:"Montserrat",sans-serif;font-weight:700;font-size:11px;letter-spacing:.5px;border-radius:20px;color:var(--white);background:var(--navy)}
.btn.gray{background:#9a9a9a}
.dotsoc{width:26px;height:26px;border-radius:50%;display:inline-block;margin-right:6px}

/* header */
.site-header{left:0;top:0;width:1200px;height:110px;background:var(--white)}
.brand{left:113px;top:30px;font-family:"Montserrat",sans-serif;font-weight:800;font-size:34px;color:var(--navy);letter-spacing:1px}
.search{left:422px;top:34px;width:354px;height:36px;border-radius:18px;background:var(--white);box-shadow:0 0 0 1px #ddd,0 2px 6px rgba(0,0,0,.12);font-size:12px;color:#777;padding:10px 22px}
.search svg{position:absolute;right:16px;top:10px}
.header-social{left:800px;top:36px;display:flex}
.signup{left:968px;top:30px;width:116px;height:40px;background:var(--sky);font-size:14px}
.main-nav{left:0;top:110px;width:1200px;height:34px;background:var(--deep-blue)}
.main-nav ul{list-style:none;display:flex;position:absolute;left:113px;top:0;height:34px;align-items:center}
.main-nav li{color:var(--white);font-family:"Montserrat",sans-serif;font-weight:600;font-size:13px;margin-right:42px}
.cart{left:968px;top:110px;width:116px;height:34px;background:#9ab4d4;color:var(--white);font-size:11px;display:flex;align-items:center;justify-content:center;gap:8px}

/* hero */
.hero{left:0;top:144px;width:1200px;height:576px;background:linear-gradient(180deg,#7c8a98 0%,#b98e5a 38%,#e2a35a 48%,#3a4554 62%,#1c2430 100%)}
.hero-title{left:520px;top:288px;font-family:"Montserrat",sans-serif;font-weight:700;font-size:84px;color:var(--white);letter-spacing:4px}
.hero-sub{left:522px;top:400px;width:570px;font-size:20px;line-height:1.6;color:var(--white)}
.hero-dots{left:524px;top:524px;display:flex;gap:10px}
.hero-dots span{width:9px;height:9px;border-radius:50%;background:var(--white)}
.hero-dots span:nth-child(3){background:transparent}

/* about */
.about{left:0;top:720px;width:1200px;height:698px;background:var(--white)}
.about-box{left:113px;top:116px;width:538px;height:460px;border:2px solid #7d7d7d}
.about-title{left:166px;top:178px;font-size:36px}
.about-text{left:166px;top:252px;width:380px;font-size:12px;line-height:2.1;color:var(--muted)}
.about-btn{left:166px;top:450px;width:150px;height:48px;font-size:12px}
.about-media{left:588px;top:156px;width:495px;height:379px;background:linear-gradient(180deg,#e9c79a 0%,#c9925a 45%,#4c3b2c 100%)}
.play{left:800px;top:300px}

/* products */
.products{left:0;top:1418px;width:1200px;height:570px;background:linear-gradient(180deg,#2f3a44 0%,#46505a 45%,#1d2730 100%)}
.products-title{left:113px;top:118px;font-size:34px;color:var(--white);font-weight:600}
.arrows{display:flex;gap:8px}
.arrow{width:30px;height:30px;border-radius:50%;border:2px solid rgba(255,255,255,.8);display:flex;align-items:center;justify-content:center}
.product-card{top:219px;width:222px;height:247px;background:var(--white)}
.product-card .thumb{position:absolute;left:30px;top:22px;width:162px;height:140px;border-radius:4px}
.product-card .name{position:absolute;left:0;width:100%;top:175px;text-align:center;font-family:"Montserrat",sans-serif;font-weight:600;font-size:13px}
.product-card .stars{position:absolute;left:0;width:100%;top:197px;text-align:center;color:var(--star);font-size:13px;letter-spacing:1px}

/* what we do */
.what{left:0;top:1988px;width:1200px;height:447px;background:var(--panel)}
.what-photo{left:0;top:0;width:720px;height:447px}
.what-title{left:737px;top:68px;font-size:36px}
.what-sub{left:737px;top:165px;font-family:"Montserrat",sans-serif;font-weight:700;font-size:17px}
.what-text{left:737px;top:205px;width:350px;font-size:12px;line-height:2.2;color:var(--muted)}
.what-btn{left:737px;top:330px;width:112px;height:38px}
.fish-badge{left:600px;top:164px;width:116px;height:116px;border-radius:50%;background:var(--white);display:flex;align-items:center;justify-content:center;box-shadow:0 2px 10px rgba(0,0,0,.12)}

/* blog */
.blog{left:0;top:2435px;width:1200px;height:1127px;background:var(--light-gray)}
.tab{top:112px;font-family:"Montserrat",sans-serif;font-size:24px;font-weight:600}
.tab.active{color:var(--navy)}
.tab.inactive{color:#888}
.blog-nav{left:890px;top:114px;display:flex;gap:8px;align-items:center}
.blog-nav .arr{width:28px;height:28px;border-radius:50%;display:flex;align-items:center;justify-content:center}
.viewall{position:relative;width:100px;height:30px;border-radius:16px;background:var(--sky);color:var(--white);font-family:"Montserrat",sans-serif;font-weight:700;font-size:10px;display:flex;align-items:center;justify-content:center;margin-left:12px}
.post{width:303px;background:var(--white);box-shadow:0 2px 8px rgba(0,0,0,.08)}
.post .pic{position:absolute;left:0;top:0;width:303px;height:185px}
.post .tag{position:absolute;left:14px;top:16px;padding:3px 10px;border-radius:10px;background:var(--orange);color:var(--white);font-size:8px;font-weight:700;font-family:"Montserrat",sans-serif}
.post .heart{position:absolute;right:12px;top:140px;width:36px;height:36px;border-radius:50%;display:flex;align-items:center;justify-content:center;border:3px solid var(--white)}
.post h3{position:absolute;left:18px;top:212px;font-family:"Montserrat",sans-serif;font-weight:600;font-size:15px}
.post p{position:absolute;left:18px;top:248px;width:265px;font-size:11px;line-height:1.9;color:#666}
.post .b1{left:18px;width:82px;height:22px;font-size:9px}
.post .b2{left:112px;width:82px;height:22px;font-size:9px}

/* gallery */
.gallery{left:0;top:3562px;width:1200px;height:538px;background:var(--white)}
.gallery-title{left:0;width:1200px;top:112px;text-align:center;font-size:34px}
.gitem{top:210px;width:232px;height:213px}

/* contact */
.contact{left:0;top:4100px;width:1200px;height:600px;background:#1b1b1b}
.contact-title{left:0;width:1200px;top:112px;text-align:center;color:var(--white);font-size:34px}
.getin{left:113px;top:188px;color:var(--white);font-family:"Montserrat",sans-serif;font-weight:600;font-size:16px}
.field{background:var(--white);font-size:10px;color:#777;padding:7px 8px}
.submit{left:640px;top:412px;width:76px;height:24px;font-size:10px}
.info-row{left:800px;display:flex;align-items:center;gap:16px;color:var(--white);font-size:12px;line-height:1.7}
.info-icon{width:38px;height:38px;border-radius:50%;border:2px solid rgba(255,255,255,.8);display:flex;align-items:center;justify-content:center;flex:none}
.contact-social{left:800px;top:400px;display:flex}
.footer-line{left:113px;top:510px;width:970px;height:1px;background:#444}
.copyright{left:0;width:1200px;top:546px;text-align:center;color:#ddd;font-size:12px}
</style>
</head>
<body>

<header class="site-header abs">
  <div class="brand abs">LOOPCAST</div>
  <div class="search abs">Search
    <svg width="16" height="16" viewBox="0 0 16 16"><circle cx="6.5" cy="6.5" r="5" fill="none" stroke="#333" stroke-width="2"/><line x1="10" y1="10" x2="15" y2="15" stroke="#333" stroke-width="2"/></svg>
  </div>
  <div class="header-social abs">
    <span class="dotsoc" style="background:#2a4f9c"></span><span class="dotsoc" style="background:#29a9e1"></span><span class="dotsoc" style="background:#d0263a"></span><span class="dotsoc" style="background:#dd4b39"></span>
  </div>
  <div class="btn signup">SIGN UP</div>
</header>

<nav class="main-nav abs">
  <ul><li>HOME</li><li>ABOUT US</li><li>PRODUCTS</li><li>CONTACT US</li><li>ARTICLES</li></ul>
</nav>
<div class="cart abs">
  <svg width="18" height="16" viewBox="0 0 18 16"><path d="M1 2h3l2 9h9l2-7H5" fill="none" stroke="#fff" stroke-width="2"/><circle cx="7" cy="14" r="1.5" fill="#fff"/><circle cx="14" cy="14" r="1.5" fill="#fff"/></svg>0 items
</div>

<section class="hero abs" role="img" aria-label="Angler reeling in a catch from a boat at sunset over the sea">
  <div class="hero-title abs">LOOPCAST</div>
  <div class="hero-sub abs">Sed ut perspiciatis unde omnis oluptatequasi architecto beatae vmccusantium atione voluptat.</div>
  <div class="hero-dots abs"><span></span><span></span><span></span><span></span><span></span></div>
</section>

<section class="about abs">
  <div class="about-box abs"></div>
  <h2 class="heading about-title abs">ABOUT <b>US</b></h2>
  <p class="about-text abs">Sed ut perspiciatis unde omnis iste natus error sit voluptatem accusan tium doloremque laudantium, totam rem aperiam, eaque ipsa quae ab illo inventore veritatis et quasi architecto beatae vitae dicta sunt explica bo. Nemo enim ipsam voluptatem quia voluptas sit aspernatur aut odit aut fugit, sed quia consequuntur magni dolores.</p>
  <div class="btn about-btn">READ MORE</div>
  <div class="about-media abs" role="img" aria-label="Angler in a hat casting a line at a lake at sunset"></div>
  <svg class="play abs" width="76" height="76" viewBox="0 0 76 76"><circle cx="38" cy="38" r="35" fill="rgba(255,255,255,.25)" stroke="#fff" stroke-width="3"/><path d="M30 24l22 14-22 14z" fill="#fff"/></svg>
</section>

<section class="products abs" role="img" aria-label="Dusk harbour with a pier and fishing rods in the foreground">
  <h2 class="products-title abs">LATEST PRODUCTS</h2>
  <div class="arrows abs" style="left:1010px;top:105px">
    <div class="arrow"><svg width="10" height="10" viewBox="0 0 10 10"><path d="M7 1L3 5l4 4" fill="none" stroke="#fff" stroke-width="2"/></svg></div>
    <div class="arrow"><svg width="10" height="10" viewBox="0 0 10 10"><path d="M3 1l4 4-4 4" fill="none" stroke="#fff" stroke-width="2"/></svg></div>
  </div>
  <div class="product-card abs" style="left:113px"><div class="thumb" role="img" aria-label="Inflatable fishing boat" style="background:linear-gradient(180deg,#fff 20%,#2e4f8e 55%,#fff 85%)"></div><div class="name">ONSEQUUNTUR</div><div class="stars">★★★★★</div></div>
  <div class="product-card abs" style="left:363px"><div class="thumb" role="img" aria-label="Metal fishing lure" style="background:linear-gradient(180deg,#fff 35%,#b9bcc2 50%,#fff 65%)"></div><div class="name">LAUDANTIUM</div><div class="stars">★★★★★</div></div>
  <div class="product-card abs" style="left:610px"><div class="thumb" role="img" aria-label="Fishing backpack" style="background:linear-gradient(90deg,#fff 25%,#2a2a2a 40%,#3b3b3b 60%,#fff 75%)"></div><div class="name">TOTAM REM</div><div class="stars">★★★★★</div></div>
  <div class="product-card abs" style="left:861px"><div class="thumb" role="img" aria-label="Small wooden sailing boat" style="background:linear-gradient(180deg,#fff 15%,#f0c85a 45%,#9b5a22 75%,#fff 90%)"></div><div class="name">APERIAM</div><div class="stars">★★★★★</div></div>
</section>

<section class="what abs">
  <svg class="what-photo abs" viewBox="0 0 720 447" role="img" aria-label="Fisherman holding a bent rod on a boat at open sea">
    <defs><linearGradient id="sea" x1="0" y1="0" x2="0" y2="1"><stop offset="0" stop-color="#6fa4d8"/><stop offset=".45" stop-color="#2f6fb0"/><stop offset="1" stop-color="#10365f"/></linearGradient></defs>
    <polygon points="0,0 620,0 700,447 0,447" fill="url(#sea)"/>
  </svg>
  <div class="fish-badge abs"><svg width="64" height="34" viewBox="0 0 64 34"><path d="M4 17c10-14 34-14 46 0-12 14-36 14-46 0z" fill="none" stroke="#0b3f86" stroke-width="3"/><path d="M50 17l12-10v20z" fill="none" stroke="#0b3f86" stroke-width="3"/><line x1="26" y1="6" x2="26" y2="28" stroke="#0b3f86" stroke-width="2"/><circle cx="14" cy="15" r="2" fill="#0b3f86"/></svg></div>
  <h2 class="heading what-title abs">WHAT <b>WE DO</b></h2>
  <div class="what-sub abs">FISHING</div>
  <p class="what-text abs">Sed ut perspiciatis unde omnis iste natus error sit voluptatem accusantium doloremque laudantium, totam rem aperiam, eaque ipsa quae ab illo inventore veritatis.</p>
  <div class="btn what-btn" style="font-size:10px">READ MORE</div>
</section>

<section class="blog abs">
  <div class="tab active abs" style="left:113px">BLOG POSTS</div>
  <div class="tab inactive abs" style="left:327px">ARTICLES</div>
  <div class="blog-nav abs">
    <div class="arr" style="background:var(--navy)"><svg width="10" height="10" viewBox="0 0 10 10"><path d="M7 1L3 5l4 4" fill="none" stroke="#fff" stroke-width="2"/></svg></div>
    <div class="arr" style="border:2px solid #999"><svg width="10" height="10" viewBox="0 0 10 10"><path d="M3 1l4 4-4 4" fill="none" stroke="#666" stroke-width="2"/></svg></div>
    <div class="viewall">VIEW ALL</div>
  </div>

  <article class="post abs" style="left:113px;top:213px;height:392px"><div class="pic" role="img" aria-label="Angler holding a large fish on a boat" style="background:linear-gradient(180deg,#9fc5e5,#3f79ad)"></div><span class="tag">BEST SELLER</span><span class="heart" style="background:var(--green)"><svg width="16" height="14" viewBox="0 0 16 14"><path d="M8 13L1.5 6.5A3.5 3.5 0 0 1 8 2a3.5 3.5 0 0 1 6.5 4.5z" fill="#fff"/></svg></span><h3>PERSPICIATIS UNDE</h3><p>But I must explain to you how all this mistaken idea of denous the great the tmcmg</p><div class="btn b1" style="top:340px">READ MORE</div><div class="btn gray b2" style="top:340px">BUY NOW</div></article>
  <article class="post abs" style="left:448px;top:213px;height:432px"><div class="pic" role="img" aria-label="Fishing trawler at sea under a cloudy sky" style="background:linear-gradient(180deg,#9eb7cf,#4d6f8f 60%,#26425e)"></div><span class="tag">BEST SELLER</span><span class="heart" style="background:var(--green)"><svg width="16" height="14" viewBox="0 0 16 14"><path d="M8 13L1.5 6.5A3.5 3.5 0 0 1 8 2a3.5 3.5 0 0 1 6.5 4.5z" fill="#fff"/></svg></span><h3>RATIONE VOLUPTATEM</h3><p>But I must explain to you how eos qui ratione voluptatem sit all this mistaken idea of denous the great flexone voluptatem.</p><div class="btn b1" style="top:380px">READ MORE</div><div class="btn gray b2" style="top:380px">BUY NOW</div></article>
  <article class="post abs" style="left:783px;top:213px;height:392px"><div class="pic" role="img" aria-label="Chinese fishing nets over calm water" style="background:linear-gradient(180deg,#c8dcea,#7fa7c4 60%,#3b5e78)"></div><span class="tag">BEST SELLER</span><span class="heart" style="background:var(--orange)"><svg width="16" height="14" viewBox="0 0 16 14"><path d="M8 13L1.5 6.5A3.5 3.5 0 0 1 8 2a3.5 3.5 0 0 1 6.5 4.5z" fill="#fff"/></svg></span><h3>ES EOSQVOLUPTATEM</h3><p>But I must explain to you how all this mistaken idea of denous the great the tmcmg</p><div class="btn b1" style="top:340px">READ MORE</div><div class="btn gray b2" style="top:340px">BUY NOW</div></article>

  <article class="post abs" style="left:113px;top:625px;height:380px"><div class="pic" role="img" aria-label="Fishing nets silhouetted against a pale sky" style="background:linear-gradient(180deg,#dfe6ea,#9aabb6 60%,#4c5d68)"></div><span class="tag">BEST SELLER</span><span class="heart" style="background:var(--green)"><svg width="16" height="14" viewBox="0 0 16 14"><path d="M8 13L1.5 6.5A3.5 3.5 0 0 1 8 2a3.5 3.5 0 0 1 6.5 4.5z" fill="#fff"/></svg></span><h3>PERSPICIATIS UNDE</h3><p>But I must explain to you how all this mistaken idea of denous the great the tmcmg</p><div class="btn b1" style="top:330px">READ MORE</div><div class="btn gray b2" style="top:330px">BUY NOW</div></article>
  <article class="post abs" style="left:448px;top:668px;height:345px"><div class="pic" role="img" aria-label="Angler on a shoreline at dusk" style="background:linear-gradient(180deg,#2d4e7a,#6c88b0 55%,#1d2f47)"></div><span class="tag">BEST SELLER</span><span class="heart" style="background:var(--red)"><svg width="16" height="14" viewBox="0 0 16 14"><path d="M8 13L1.5 6.5A3.5 3.5 0 0 1 8 2a3.5 3.5 0 0 1 6.5 4.5z" fill="#fff"/></svg></span><h3>RATIONE VOLUPTATEM</h3><p>But I must explain to you how eos qui ratione</p><div class="btn b1" style="top:296px">READ MORE</div><div class="btn gray b2" style="top:296px">BUY NOW</div></article>
  <article class="post abs" style="left:783px;top:625px;height:380px"><div class="pic" role="img" aria-label="Angler holding a rod with a lake behind" style="background:linear-gradient(180deg,#8aa9b5,#4d6b73 60%,#26363c)"></div><span class="tag">BEST SELLER</span><span class="heart" style="background:var(--green)"><svg width="16" height="14" viewBox="0 0 16 14"><path d="M8 13L1.5 6.5A3.5 3.5 0 0 1 8 2a3.5 3.5 0 0 1 6.5 4.5z" fill="#fff"/></svg></span><h3>ES EOSQVOLUPTATEM</h3><p>But I must explain to you how all this mistaken idea of denous the great the tmcmg</p><div class="btn b1" style="top:330px">READ MORE</div><div class="btn gray b2" style="top:330px">BUY NOW</div></article>
</section>

<section class="gallery abs">
  <h2 class="heading gallery-title abs">OUR <b>GALLERY</b></h2>
  <svg class="abs" style="left:48px;top:290px" width="20" height="60" viewBox="0 0 20 60"><path d="M18 2L2 30l16 28" fill="none" stroke="#aaa" stroke-width="2"/></svg>
  <svg class="abs" style="left:1132px;top:290px" width="20" height="60" viewBox="0 0 20 60"><path d="M2 2l16 28-16 28" fill="none" stroke="#aaa" stroke-width="2"/></svg>
  <div class="gitem abs" style="left:113px;background:linear-gradient(180deg,#6f8f5a,#3e5d6d)" role="img" aria-label="Two anglers in life jackets on a boat"></div>
  <div class="gitem abs" style="left:362px;background:linear-gradient(180deg,#c7b56a,#2f6a78 60%,#1b3a42)" role="img" aria-label="Fish swimming underwater in sunlit water"></div>
  <div class="gitem abs" style="left:608px;background:linear-gradient(180deg,#4d6b3a,#8a7a45 60%,#2c2a1e)" role="img" aria-label="Excited angler holding up a fish"></div>
  <div class="gitem abs" style="left:854px;background:linear-gradient(180deg,#8eb8d6,#6f6a50 60%,#3a3f30)" role="img" aria-label="Angler holding a spotted trout"></div>
</section>

<footer class="contact abs">
  <h2 class="heading contact-title abs">CONTACT US</h2>
  <div class="getin abs">Get In Touch:</div>
  <div class="field abs" style="left:113px;top:232px;width:296px;height:30px">NAME :</div>
  <div class="field abs" style="left:420px;top:232px;width:296px;height:30px">PHONE :</div>
  <div class="field abs" style="left:113px;top:272px;width:603px;height:30px">EMAIL :</div>
  <div class="field abs" style="left:113px;top:312px;width:603px;height:78px">MESSAGE :</div>
  <div class="btn submit">SUBMIT</div>

  <div class="info-row abs" style="top:222px"><span class="info-icon"><svg width="14" height="18" viewBox="0 0 14 18"><path d="M7 17S1 10 1 6.5a6 6 0 0 1 12 0C13 10 7 17 7 17z" fill="#fff"/><circle cx="7" cy="6.5" r="2" fill="#1b1b1b"/></svg></span><span>133 Veritatis et quasi architecto<br>beatae vitae dic.</span></div>
  <div class="info-row abs" style="top:285px"><span class="info-icon"><svg width="16" height="16" viewBox="0 0 16 16"><path d="M3 1l3 3-2 2c1 2 3 4 5 5l2-2 3 3-2 3C7 15 1 9 1 3z" fill="#fff"/></svg></span><span>Phone : 1 555 014 2277</span></div>
  <div class="info-row abs" style="top:334px"><span class="info-icon"><svg width="16" height="12" viewBox="0 0 16 12"><rect x="1" y="1" width="14" height="10" fill="#fff"/><path d="M1 1l7 6 7-6" fill="none" stroke="#1b1b1b" stroke-width="1.5"/></svg></span><span>Email : info@lakeline.example</span></div>
  <div class="contact-social abs">
    <span class="dotsoc" style="background:#2a4f9c"></span><span class="dotsoc" style="background:#29a9e1"></span><span class="dotsoc" style="background:#d0263a"></span><span class="dotsoc" style="background:#dd4b39"></span><span class="dotsoc" style="background:#0e76a8"></span><span class="dotsoc" style="background:#e52d27"></span>
  </div>
  <div class="footer-line abs"></div>
  <div class="copyright abs">Copyright © 2018 - Lakeline Studio - All rights reserved &nbsp;|&nbsp; Privacy policy</div>
</footer>

</body>
</html>
```